Federal Government Proposal Development Consulting company needs a website designed and coded

I am looking for someone to design (using an existing logo, color palette, and text fonts) and code a wordpress-based website for a Proposal Development consulting company. I have full copy for all site pages and suggestions for images/ graphics and a few example design templates to go from.

One note, from a color perspective - I included a mockup of a business card to highlight a color scheme that I tend to like - if you look at the back of the business card, the blend of the grey, blue, with the neon green highlight as a separator really seems to pop. Just a thought as you are designing the page.

I would like to see 2-3 potential design layouts, and I will select one to move forward with. Then, I would like the site to be coded for WordPress (I can provide a login to my wordpress site). I would like 1 opportunity to review the coded site and make any final tweaks.

```html
<!DOCTYPE html>
<html lang="en">
<head>
<meta charset="utf-8">
<title>Northvale Bid Partners LLC</title>
<link rel="stylesheet" href="https://fonts.googleapis.com/css2?family=Alegreya:wght@400;500&family=Jost:wght@300;400;500&display=swap">
<style>
:root{
  --navy:#13124c;
  --navy-deep:#0d0c33;
  --mint:#06f5c6;
  --grey:#85858f;
  --grey-light:#f6f6f8;
  --text:#4a4a55;
  --muted:#8d8d97;
  --white:#ffffff;
}
*{box-sizing:border-box;margin:0;padding:0}
html,body{width:1200px;height:4149px;overflow:hidden}
body{position:relative;font-family:"Jost",sans-serif;color:var(--text);background:var(--white)}
.abs{position:absolute}
.serif{font-family:"Alegreya",serif;font-weight:400}
.btn{position:absolute;background:var(--mint);color:var(--navy);font-size:14px;text-transform:uppercase;display:flex;align-items:center;justify-content:center;border-radius:8px}

/* header */
.topbar{position:absolute;left:411px;top:0;width:789px;height:48px;background:var(--navy);clip-path:polygon(0 0,100% 0,100% 100%,36px 100%)}
.topbar .item{position:absolute;top:14px;color:var(--white);font-size:16px;display:flex;gap:10px;align-items:center}
.social{position:absolute;top:15px;display:flex;gap:16px}
.social span{width:18px;height:18px;border-radius:50%;background:currentColor;display:block}
.wordmark{position:absolute;display:flex;align-items:center;gap:10px;font-family:"Jost",sans-serif;font-weight:400;white-space:nowrap;line-height:1}
.wordmark .dot{width:14px;height:14px;border-radius:50%;background:currentColor;flex:none}
.nav{position:absolute;top:72px;right:114px;display:flex;gap:34px;font-size:17px;color:var(--text)}
.header-line{position:absolute;top:116px;left:0;width:1200px;height:1px;background:#e4e4ea}

/* hero */
.hero{position:absolute;top:117px;left:0;width:1200px;height:556px;background:#ececef}
.hero-photo{position:absolute;left:600px;top:0;width:600px;height:556px;background:radial-gradient(circle at 55% 50%,#c7c9cf 0,#dadbe0 40%,#ececef 75%)}
.hero h1{position:absolute;left:111px;top:158px;font-size:46px;color:var(--navy)}
.hero p{position:absolute;left:111px;top:226px;width:500px;font-size:27px;line-height:35px;color:var(--navy-deep);font-weight:300}

/* what we do */
.section-title{position:absolute;left:0;width:1200px;text-align:center;font-size:40px;color:var(--navy)}
.intro{position:absolute;left:150px;top:816px;width:900px;text-align:center;font-size:15.5px;line-height:26px;color:var(--muted);font-weight:300}
.card-base{position:absolute;top:1063px;width:300px;height:197px;background:var(--navy);clip-path:polygon(0 0,27px 20px,273px 20px,300px 0,300px 100%,0 100%)}
.card-base.lift{background:#f1f1f4;box-shadow:0 6px 14px rgba(0,0,0,.15);clip-path:none}
.card{position:absolute;top:990px;width:251px;height:246px;background:var(--grey);border-radius:6px;color:var(--white);padding:0 17px}
.card.active{background:var(--mint);color:var(--navy)}
.card svg{display:block;margin:14px auto 0}
.card h3{font-family:"Alegreya",serif;font-weight:400;font-size:22px;text-align:center;margin-top:10px}
.card p{font-size:13px;line-height:26px;margin-top:12px}

/* who we are */
.who{position:absolute;top:1345px;left:0;width:1200px;height:527px;background:var(--navy)}
.who-circle{position:absolute;left:111px;top:88px;width:178px;height:178px;border-radius:50%;background:var(--mint)}
.who-photo{position:absolute;left:182px;top:161px;width:366px;height:279px;background:linear-gradient(135deg,#6b5042,#a58b73 45%,#e7e2dc)}
.who h2{position:absolute;left:599px;top:155px;font-size:40px;color:var(--white)}
.who p{position:absolute;left:599px;top:218px;width:489px;color:var(--white);font-size:16px;line-height:26px;font-weight:300;text-align:justify}

/* services */
.services{position:absolute;top:1872px;left:0;width:1200px;height:759px;background:var(--grey-light)}
.svc{position:absolute;width:220px;height:156px;border:2px dashed #6d6d78}
.svc.active{border:2px solid var(--navy)}
.svc::before,.svc::after{content:"";position:absolute;top:48px;width:5px;height:50px;background:var(--mint)}
.svc::before{left:-4px}.svc::after{right:-4px}
.svc.active::before,.svc.active::after{background:var(--navy)}
.svc .ring{position:absolute;left:44px;top:-44px;width:128px;height:128px;border-radius:50%;background:var(--white);border:2px solid var(--navy);display:flex;align-items:center;justify-content:center}
.svc .disc{width:108px;height:108px;border-radius:50%;background:var(--grey);display:flex;align-items:center;justify-content:center}
.svc.active .disc{background:var(--mint)}
.svc .label{position:absolute;left:0;top:98px;width:100%;text-align:center;font-size:21px;line-height:24px;color:var(--navy-deep)}

/* contact */
.contact{position:absolute;top:2631px;left:0;width:1200px;height:585px;background:var(--navy)}
.contact h2{position:absolute;left:111px;top:78px;font-size:40px;color:var(--white)}
.contact .lead{position:absolute;left:111px;top:146px;width:390px;color:var(--white);font-size:16px;line-height:26px;font-weight:300}
.c-row{position:absolute;left:111px;display:flex;gap:33px;color:var(--white);font-size:16px;line-height:24px;font-weight:300}
.c-row svg{flex:none;margin-top:3px}
.c-divider{position:absolute;left:163px;top:298px;width:265px;height:1px;background:rgba(255,255,255,.2)}
.field{position:absolute;left:601px;width:488px;height:52px;border:1px solid rgba(255,255,255,.75);border-radius:8px;color:var(--white);font-size:16px;display:flex;align-items:center;gap:12px;padding-left:24px;font-weight:300}
.field.msg{height:108px;align-items:flex-start;padding-top:16px}

/* testimonials */
.t-card{position:absolute;top:3383px;width:317px;height:218px;background:#f6f6f8;border-radius:16px;padding:24px 27px}
.t-card.lead{background:var(--white);box-shadow:0 4px 18px rgba(0,0,0,.15)}
.quote{width:46px;height:46px;border-radius:50%;border:2px solid #b9b9c2;display:flex;align-items:center;justify-content:center;font-family:"Alegreya",serif;font-size:44px;color:#b9b9c2;line-height:1;padding-top:16px}
.lead .quote{border-color:var(--navy);color:var(--navy)}
.t-name{position:absolute;right:30px;top:26px;font-family:"Alegreya",serif;font-size:18px;color:#444;text-align:right}
.stars{font-size:12px;color:#e0a21a;letter-spacing:1px;display:block}
.t-card p{margin-top:18px;font-size:15px;line-height:24px;text-align:justify;color:#555}
.dots{position:absolute;top:3648px;left:558px;display:flex;gap:5px}
.dots span{width:17px;height:17px;border-radius:50%;background:#bbb}
.dots span:first-child{background:var(--mint)}

/* footer */
.footer{position:absolute;top:3754px;left:0;width:1200px;height:395px;background:linear-gradient(180deg,#0c0c22,#14143a)}
.footer h4{position:absolute;top:94px;font-family:"Alegreya",serif;font-weight:400;font-size:23px;color:var(--white)}
.footer .links{position:absolute;top:132px;color:var(--white);font-size:16px;line-height:26px;font-weight:300}
.footer .about{position:absolute;left:111px;top:189px;width:292px;color:var(--white);font-size:15.5px;line-height:26px;font-weight:300;text-align:justify}
.footer .rule{position:absolute;left:111px;top:338px;width:978px;height:1px;background:rgba(255,255,255,.25)}
.footer .copy{position:absolute;left:0;top:357px;width:1200px;text-align:center;font-family:"Alegreya",serif;font-size:15px;color:var(--white)}
</style>
</head>
<body>

<!-- header -->
<div class="wordmark" style="left:113px;top:40px;font-size:24px;color:var(--navy)"><span class="dot"></span>Northvale Bid Partners</div>
<div class="topbar">
  <div class="item" style="left:92px">
    <svg width="15" height="15" viewBox="0 0 24 24" fill="#fff"><path d="M6.6 10.8a15 15 0 0 0 6.6 6.6l2.2-2.2a1 1 0 0 1 1-.25 11.4 11.4 0 0 0 3.6.57 1 1 0 0 1 1 1V20a1 1 0 0 1-1 1A17 17 0 0 1 3 4a1 1 0 0 1 1-1h3.5a1 1 0 0 1 1 1c0 1.25.2 2.45.57 3.57a1 1 0 0 1-.25 1z"/></svg>(555) 014-2739</div>
  <div class="item" style="left:288px">
    <svg width="16" height="12" viewBox="0 0 24 18" fill="#fff"><path d="M0 0h24v2L12 10 0 2z"/><path d="M0 4l12 8 12-8v14H0z"/></svg>hello@northvalebid.example</div>
  <div class="social" style="left:552px;color:#fff" aria-label="Social links"><span></span><span></span><span></span><span></span></div>
</div>
<nav class="nav"><span>Home</span><span>Work With Us</span><span>Work For Us</span><span>About Us</span><span>Contact</span></nav>
<div class="header-line"></div>

<!-- hero -->
<section class="hero">
  <div class="hero-photo" role="img" aria-label="Overhead photo of a team meeting around a table with charts"></div>
  <h1 class="serif">Generate Success:</h1>
  <p>Fuel Innovation in Proposal Excellence with Northvale! Click here to explore our services.</p>
  <div class="btn" style="left:111px;top:357px;width:181px;height:38px">Get Started</div>
</section>

<!-- what we do -->
<h2 class="section-title serif" style="top:748px">What We Do</h2>
<p class="intro">Northvale Bid Partners, specializes in advancing an organization through a comprehensive suite of services designed to modernize the proposal development process. From innovative Capture Management strategies that pinpoint lucrative opportunities, meticulous Proposal Development services that transform concepts into effective narratives, and cutting-edge Generative AI techniques that create domain-aware content accelerating proposal draft development, we are your dedicated partner in securing success.</p>

<div class="card-base" style="left:124px"></div>
<div class="card-base lift" style="left:451px"></div>
<div class="card-base" style="left:776px"></div>

<div class="card" style="left:151px">
  <svg width="72" height="70" viewBox="0 0 72 70" fill="none" stroke="#fff" stroke-width="2"><rect x="4" y="4" width="34" height="44" rx="2"/><path d="M10 14h22M10 22h22M10 30h14"/><rect x="30" y="30" width="36" height="34" rx="2"/><path d="M38 56v-8M46 56v-14M54 56v-10"/></svg>
  <h3>Capture Management</h3>
  <p>Elevate your business development strategy with our Capture Management services.</p>
</div>
<div class="card active" style="left:477px">
  <svg width="60" height="70" viewBox="0 0 60 70" fill="none" stroke="#13124c" stroke-width="2"><rect x="4" y="4" width="52" height="62" rx="2"/><circle cx="30" cy="24" r="9"/><path d="M26 34h8M27 38h6M14 48h32M14 54h32M14 60h32"/></svg>
  <h3>Proposal Development</h3>
  <p>Transform your vision into winning proposals with our Proposal Development services.</p>
  <svg class="abs" style="left:216px;top:210px;margin:0" width="26" height="26" viewBox="0 0 26 26"><path d="M10 10l14 5-6 2-2 6z" fill="#13124c"/><path d="M6 2v4M1 7h4M2 2l3 3" stroke="#13124c" stroke-width="1.5"/></svg>
</div>
<div class="card" style="left:804px">
  <svg width="66" height="70" viewBox="0 0 66 70" fill="none" stroke="#fff" stroke-width="2"><rect x="12" y="4" width="42" height="62" rx="3"/><rect x="4" y="22" width="26" height="24" rx="2"/><rect x="10" y="28" width="14" height="12"/><path d="M36 14h12M36 20h12M54 40h8M54 48h8"/></svg>
  <h3>Generative AI</h3>
  <p>Revolutionize your proposal writing process with our domain-aware Generative AI</p>
</div>

<!-- who we are -->
<section class="who">
  <div class="who-circle"></div>
  <div class="who-photo" role="img" aria-label="Photo of a woman writing notes at a desk beside a laptop"></div>
  <h2 class="serif">Who We Are</h2>
  <p>Sed ut perspiciatis unde omnis iste natus error sit voluptatem accusantium doloremque laudantium, totam rem aperiam, eaque ipsa quae ab illo inventore veritatis et quasi architecto beatae vitae dicta sunt explicabo. Nemo enim ipsam voluptatem quia voluptas sit aspernatur aut</p>
  <div class="btn" style="left:599px;top:372px;width:123px;height:39px">Read More</div>
</section>

<!-- services -->
<section class="services">
  <h2 class="section-title serif" style="top:78px">Our Services</h2>

  <div class="svc" style="left:121px;top:195px"><div class="ring"><div class="disc"><svg width="60" height="52" viewBox="0 0 60 52" fill="none" stroke="#fff" stroke-width="2"><path d="M4 12V4h8M48 4h8v8M4 40v8h8M56 40v8h-8"/><path d="M16 18h12l3 4h14v20H16z"/></svg></div></div><div class="label">Capture<br>Management</div></div>
  <div class="svc active" style="left:367px;top:195px"><div class="ring"><div class="disc"><svg width="60" height="52" viewBox="0 0 60 52" fill="none" stroke="#13124c" stroke-width="2.2"><path d="M52 4C36 8 26 20 22 36l6 2C34 24 44 14 52 4z"/><path d="M22 36l-4 8"/><rect x="6" y="30" width="14" height="16" rx="2"/><path d="M38 36l12 5-5 2-2 5z" fill="#13124c"/></svg></div></div><div class="label">Technical<br>Writer</div></div>
  <div class="svc" style="left:614px;top:195px"><div class="ring"><div class="disc"><svg width="56" height="56" viewBox="0 0 56 56" fill="none" stroke="#fff" stroke-width="2"><rect x="8" y="8" width="32" height="42" rx="2"/><path d="M18 4h12v8H18zM14 20h4M22 20h14M14 28h4M22 28h14M14 36h4M22 36h10"/><path d="M36 30l10 18H26z"/></svg></div></div><div class="label">Compliance<br>Reviews</div></div>
  <div class="svc" style="left:860px;top:195px"><div class="ring"><div class="disc"><svg width="56" height="56" viewBox="0 0 56 56" fill="none" stroke="#fff" stroke-width="2"><circle cx="28" cy="18" r="10"/><path d="M22 18l6-6 6 6-6 6z"/><path d="M6 40c8-6 14-4 20 0h12c2 0 2 4 0 4H26M6 48l8-4c6 4 18 6 32-6"/></svg></div></div><div class="label">Proposal<br>Management</div></div>

  <div class="svc" style="left:121px;top:427px"><div class="ring"><div class="disc"><svg width="56" height="56" viewBox="0 0 56 56" fill="none" stroke="#fff" stroke-width="2"><rect x="8" y="6" width="34" height="44" rx="2"/><path d="M14 16h20M14 24h20M14 32h20M14 40h12"/><path d="M48 14L34 44l-3 4 1-5 14-30z"/></svg></div></div><div class="label">Resume<br>Writer</div></div>
  <div class="svc" style="left:367px;top:427px"><div class="ring"><div class="disc"><svg width="56" height="56" viewBox="0 0 56 56" fill="none" stroke="#fff" stroke-width="2"><circle cx="28" cy="28" r="18" stroke-dasharray="6 3"/><circle cx="28" cy="28" r="12"/><path d="M22 34v-6M28 34V22M34 34v-8"/></svg></div></div><div class="label">Proposal<br>Production</div></div>
  <div class="svc" style="left:614px;top:427px"><div class="ring"><div class="disc"><svg width="60" height="52" viewBox="0 0 60 52" fill="none" stroke="#fff" stroke-width="2"><rect x="4" y="6" width="52" height="40" rx="2"/><path d="M4 14h52"/><path d="M48 20L30 30l6 3 2 7z"/><path d="M10 38c6-8 12 4 18-4"/></svg></div></div><div class="label">Desktop<br>Publishing</div></div>
  <div class="svc" style="left:860px;top:427px"><div class="ring"><div class="disc"><svg width="56" height="56" viewBox="0 0 56 56" fill="none" stroke="#fff" stroke-width="3"><path d="M30 10H12a2 2 0 0 0-2 2v32a2 2 0 0 0 2 2h32a2 2 0 0 0 2-2V26"/><path d="M42 6l8 8-20 20-10 2 2-10z"/></svg></div></div><div class="label">White Glove<br>Editing</div></div>

  <div class="btn" style="left:538px;top:633px;width:122px;height:40px">View All</div>
</section>

<!-- contact -->
<section class="contact">
  <h2 class="serif">Contact Us</h2>
  <p class="lead">Sed ut perspiciatis unde omnis iste natus error sit voluptatem accusantium</p>
  <div class="c-row" style="top:240px"><svg width="18" height="18" viewBox="0 0 24 24" fill="#fff"><path d="M22 2L2 11l8 3 3 8z"/></svg><span>Lorem ipsum dolor sit amet, consectetur<br>adipiscing elit, sed do</span></div>
  <div class="c-divider"></div>
  <div class="c-row" style="top:326px"><svg width="18" height="18" viewBox="0 0 24 24" fill="#fff"><path d="M6.6 10.8a15 15 0 0 0 6.6 6.6l2.2-2.2a1 1 0 0 1 1-.25 11.4 11.4 0 0 0 3.6.57 1 1 0 0 1 1 1V20a1 1 0 0 1-1 1A17 17 0 0 1 3 4a1 1 0 0 1 1-1h3.5a1 1 0 0 1 1 1c0 1.25.2 2.45.57 3.57a1 1 0 0 1-.25 1z"/></svg><span>Phone no: (555) 014-2739</span></div>
  <div class="c-row" style="top:362px"><svg width="18" height="14" viewBox="0 0 24 18" fill="#fff"><path d="M0 0h24v2L12 10 0 2z"/><path d="M0 4l12 8 12-8v14H0z"/></svg><span>Mail: hello@northvalebid.example</span></div>

  <div class="field" style="top:85px"><svg width="14" height="14" viewBox="0 0 24 24" fill="#fff"><circle cx="12" cy="7" r="6"/><path d="M0 24c0-7 5-10 12-10s12 3 12 10z"/></svg>Enter name</div>
  <div class="field" style="top:163px"><svg width="14" height="14" viewBox="0 0 24 24" fill="#fff"><path d="M6.6 10.8a15 15 0 0 0 6.6 6.6l2.2-2.2a1 1 0 0 1 1-.25 11.4 11.4 0 0 0 3.6.57 1 1 0 0 1 1 1V20a1 1 0 0 1-1 1A17 17 0 0 1 3 4a1 1 0 0 1 1-1h3.5a1 1 0 0 1 1 1c0 1.25.2 2.45.57 3.57a1 1 0 0 1-.25 1z"/></svg>Enter phone</div>
  <div class="field" style="top:241px"><svg width="14" height="11" viewBox="0 0 24 18" fill="#fff"><path d="M0 0h24v2L12 10 0 2z"/><path d="M0 4l12 8 12-8v14H0z"/></svg>Enter email</div>
  <div class="field msg" style="top:311px">Enter message</div>
  <div class="btn" style="left:601px;top:457px;width:121px;height:39px">Submit</div>
</section>

<!-- testimonials -->
<h2 class="section-title serif" style="top:3297px">Our Testimonials</h2>
<div class="t-card" style="left:-253px"><div class="t-name">- Alexander<span class="stars">★★★★☆</span></div><div class="quote">“</div><p>Lorem ipsum dolor sit amet, consectetur adipiscing elit, sed do eiusmod tempor incididunt ut labore et dolore magna aliqua.</p></div>
<div class="t-card lead" style="left:95px"><div class="t-name">- Alexander<span class="stars">★★★★☆</span></div><div class="quote">“</div><p>Lorem ipsum dolor sit amet, consectetur adipiscing elit, sed do eiusmod tempor incididunt ut labore et dolore magna aliqua.</p></div>
<div class="t-card" style="left:441px"><div class="t-name">- Alexander<span class="stars">★★★★☆</span></div><div class="quote">“</div><p>Lorem ipsum dolor sit amet, consectetur adipiscing elit, sed do eiusmod tempor incididunt ut labore et dolore magna aliqua.</p></div>
<div class="t-card" style="left:788px"><div class="t-name">- Alexander<span class="stars">★★★★☆</span></div><div class="quote">“</div><p>Lorem ipsum dolor sit amet, consectetur adipiscing elit, sed do eiusmod tempor incididunt ut labore et dolore magna aliqua.</p></div>
<div class="t-card" style="left:1136px"><div class="t-name">- Alexander<span class="stars">★★★★☆</span></div><div class="quote">“</div><p>Lorem ipsum dolor sit amet, consectetur adipiscing elit, sed do eiusmod tempor incididunt ut labore et dolore magna aliqua.</p></div>
<div class="dots"><span></span><span></span><span></span><span></span></div>

<!-- footer -->
<footer class="footer">
  <div class="wordmark" style="left:111px;top:104px;font-size:22px;color:var(--white)"><span class="dot"></span>Northvale Bid Partners</div>
  <p class="about">Lorem ipsum dolor sit amet, consectetur adipiscing elit, sed do eiusmod tempor incididunt ut labore et dolore magna aliqua.</p>
  <h4 style="left:472px">Quick Links</h4>
  <div class="links" style="left:472px">Home<br>Work with Us<br>Work For Us<br>About Us<br>Contact Us</div>
  <h4 style="left:652px">Contact Details</h4>
  <div class="links" style="left:652px">Phone: (555) 014-2739<br>Email: hello@northvalebid.example</div>
  <h4 style="left:950px">Follow Us</h4>
  <div class="social" style="left:950px;top:140px;color:#fff;gap:18px" aria-label="Social links"><span style="width:22px;height:22px"></span><span style="width:22px;height:22px"></span><span style="width:22px;height:22px"></span><span style="width:22px;height:22px"></span></div>
  <div class="rule"></div>
  <div class="copy">Copyright 2023 Northvale Bid Partners LLC. All Rights Reserved.</div>
</footer>

</body>
</html>
```